Redesign Video/PIcture Check in Page

Redesign our current TallyPointApp iPhone App checkin screens - Keep the design simple so that programmers do not have to do too much extra work to make your design work. - Look at the attached website screenshot for the overall look and feel, and color scheme - Convert the attached vector logo to iOS Icon format. - Deliver all graphics in the density required for iPhone XS Max. I will upload current check in pages that need to be reimagined. Check in needs to be more intutitive. Would like to add some gamification to the verification screen where they currently are required to enter series of random numbers. simple card game etc might work better. See TallyPointapp in itunes and google play store. also visit vormlink.example or tallypointapp.example for more information about our company.
The Current Checkin Process:
A. Client receives alert to checkin or submits voluntary checkin
B. Clicks checkin button on home Screen.
Redesign from here:
C. Clicks on a check in from check in list screen(new screen)
D. Enters verification number(gamification something better than random numbers)
E. Opens Camera
D. Takes Selfie
F. submits photo
G. clicks check in
SEE CURRENT STEPS PIC I UPLOADED

Target Market(s)

Courts,Probation and parole,Attorneys,Sheriffs,Jails, Alternative sentencing

Colors
3277b5

Requirements
Must have
• Must be easy to navigate,Intuitive!
Nice to have
• Gamification of check in verification.
• Step by step process with next button or similar

```html
<!DOCTYPE html>
<html lang="en">
<head>
<meta charset="utf-8">
<title>TallyPointApp – Check ins &amp; Court Dates</title>
<link href="https://fonts.googleapis.com/css2?family=Heebo:wght@200;400;500;600&display=swap" rel="stylesheet">
<style>
  :root {
    --navy: #0d2c6c;
    --alert-red: #f0281e;
    --text-dark: #4a4a4a;
    --text-muted: #a6a6a6;
    --divider: #e3e3e3;
    --screen: #ffffff;
    --backdrop: #f6f7f9;
    --avatar-tone: #8a7b70;
  }
  * { box-sizing: border-box; margin: 0; padding: 0; }
  html, body { width: 1200px; height: 1200px; overflow: hidden; }
  body {
    background: var(--backdrop);
    font-family: "Heebo", "Helvetica Neue", Arial, sans-serif;
    position: relative;
  }
  .screen {
    position: absolute;
    top: 58px;
    width: 493px;
    height: 1066px;
    background: var(--screen);
    border-radius: 56px;
    box-shadow: 0 8px 40px rgba(13, 44, 108, 0.06);
    overflow: hidden;
  }
  .screen--checkins { left: 56px; }
  .screen--court { left: 613px; }

  .top-bar {
    position: absolute;
    top: 58px;
    left: 36px;
    right: 28px;
    height: 62px;
    display: flex;
    align-items: center;
  }
  .menu-icon { width: 42px; height: 24px; }
  .user-name {
    margin-left: auto;
    margin-right: 20px;
    font-size: 17.5px;
    font-weight: 500;
    color: var(--text-dark);
  }
  .avatar {
    width: 61px; height: 61px;
    border-radius: 50%;
    background: radial-gradient(circle at 45% 40%, #b9a89a 0%, var(--avatar-tone) 55%, #4c4540 100%);
  }

  .page-title {
    position: absolute;
    top: 147px;
    left: 34px;
    font-size: 52px;
    line-height: 1.2;
    font-weight: 200;
    letter-spacing: -1.5px;
    color: var(--navy);
  }

  .entry-list {
    position: absolute;
    top: 223px;
    left: 50px;
    right: 0;
    list-style: none;
  }
  .entry {
    height: 87.3px;
    border-bottom: 1px solid var(--divider);
    position: relative;
    padding-top: 23px;
  }
  .entry-title {
    font-size: 22.5px;
    font-weight: 500;
    color: var(--text-dark);
    line-height: 1.2;
  }
  .entry-title--date { color: var(--alert-red); }
  .entry-meta {
    font-size: 17px;
    line-height: 1.2;
    font-weight: 400;
    color: var(--text-muted);
  }
  .entry-icon {
    position: absolute;
    right: 44px;
    top: 50%;
    transform: translateY(-50%);
    width: 40px; height: 40px;
  }

  .tab-bar {
    position: absolute;
    top: 954px;
    left: 0; right: 0;
    height: 112px;
    border-top: 1px solid var(--divider);
    display: flex;
    justify-content: space-around;
    padding: 20px 20px 0;
  }
  .tab {
    display: flex;
    flex-direction: column;
    align-items: center;
    width: 90px;
    font-size: 14px;
    font-weight: 500;
    color: var(--text-muted);
  }
  .tab svg { width: 34px; height: 34px; margin-bottom: 10px; }
  .tab--active { color: var(--navy); font-weight: 600; }
</style>
</head>
<body>

<svg width="0" height="0" style="position:absolute" aria-hidden="true">
  <defs>
    <symbol id="icon-pin" viewBox="0 0 40 40">
      <path d="M20 37 C12 27 7.5 21 7.5 14.5 A12.5 12.5 0 0 1 32.5 14.5 C32.5 21 28 27 20 37 Z" fill="none" stroke="#4a4a4a" stroke-width="2.6" stroke-linejoin="round"/>
      <circle cx="20" cy="14.5" r="4.5" fill="none" stroke="#4a4a4a" stroke-width="2.6"/>
    </symbol>
    <symbol id="icon-done" viewBox="0 0 40 40">
      <circle cx="20" cy="20" r="19" fill="#0d2c6c"/>
      <path d="M11.5 20.5 L17.5 26 L28.5 14.5" fill="none" stroke="#fff" stroke-width="3.6" stroke-linecap="round" stroke-linejoin="round"/>
    </symbol>
    <symbol id="icon-video" viewBox="0 0 40 40">
      <rect x="1.5" y="10" width="28" height="20" fill="none" stroke="#4a4a4a" stroke-width="2.8"/>
      <path d="M29.5 20 L38.5 12 V28 Z" fill="none" stroke="#4a4a4a" stroke-width="2.8" stroke-linejoin="round"/>
    </symbol>
    <symbol id="icon-menu" viewBox="0 0 42 24">
      <rect x="0" y="0" width="42" height="3.4" rx="1.7" fill="#0d2c6c"/>
      <rect x="0" y="10" width="36" height="3.4" rx="1.7" fill="#0d2c6c"/>
      <rect x="0" y="20" width="30" height="3.4" rx="1.7" fill="#0d2c6c"/>
    </symbol>
    <symbol id="icon-home" viewBox="0 0 36 36">
      <path d="M4 17 L18 4 L32 17 M8 14 V32 H15 V23 H21 V32 H28 V14" fill="none" stroke="#7a7a7a" stroke-width="2.4" stroke-linejoin="round" stroke-linecap="round"/>
    </symbol>
    <symbol id="icon-checkin" viewBox="0 0 36 36">
      <path d="M15 31 C9 24 5 19 5 14 A10 10 0 0 1 25 14" fill="none" stroke="#0d2c6c" stroke-width="2.4" stroke-linecap="round"/>
      <circle cx="15" cy="14" r="4" fill="none" stroke="#0d2c6c" stroke-width="2.4"/>
      <path d="M17 26 L21 30 L30 20" fill="none" stroke="#0d2c6c" stroke-width="2.4" stroke-linecap="round" stroke-linejoin="round"/>
      <circle cx="27" cy="6" r="5.5" fill="#f0281e"/>
    </symbol>
    <symbol id="icon-map" viewBox="0 0 36 36">
      <path d="M3 8 L12 4 L24 8 L33 4 V28 L24 32 L12 28 L3 32 Z M12 4 V28 M24 8 V32" fill="none" stroke="#7a7a7a" stroke-width="2.4" stroke-linejoin="round"/>
    </symbol>
    <symbol id="icon-info" viewBox="0 0 36 36">
      <circle cx="18" cy="18" r="15" fill="none" stroke="#7a7a7a" stroke-width="2.4"/>
      <circle cx="19" cy="10.5" r="1.8" fill="#7a7a7a"/>
      <path d="M16 16 H19 L17 26 H20" fill="none" stroke="#7a7a7a" stroke-width="2.4" stroke-linecap="round" stroke-linejoin="round"/>
    </symbol>
  </defs>
</svg>

<section class="screen screen--checkins">
  <header class="top-bar">
    <svg class="menu-icon"><use href="#icon-menu"/></svg>
    <span class="user-name">Marcus D Ellery</span>
    <div class="avatar" role="img" aria-label="User profile photo"></div>
  </header>
  <h1 class="page-title">Check ins</h1>
  <ul class="entry-list">
    <li class="entry"><p class="entry-title">Voluntary Check-in Request</p><p class="entry-meta">20 Oct 2018 10:27:59</p><svg class="entry-icon"><use href="#icon-pin"/></svg></li>
    <li class="entry"><p class="entry-title">Voluntary Check-in Request</p><p class="entry-meta">20 Oct 2018 10:27:59</p><svg class="entry-icon"><use href="#icon-done"/></svg></li>
    <li class="entry"><p class="entry-title">Voluntary Check-in Request</p><p class="entry-meta">20 Oct 2018 10:27:59</p><svg class="entry-icon"><use href="#icon-pin"/></svg></li>
    <li class="entry"><p class="entry-title">Voluntary Check-in Request</p><p class="entry-meta">20 Oct 2018 10:27:59</p><svg class="entry-icon"><use href="#icon-done"/></svg></li>
    <li class="entry"><p class="entry-title">Voluntary Check-in Request</p><p class="entry-meta">20 Oct 2018 10:27:59</p><svg class="entry-icon"><use href="#icon-done"/></svg></li>
    <li class="entry"><p class="entry-title">Voluntary Check-in Request</p><p class="entry-meta">20 Oct 2018 10:27:59</p><svg class="entry-icon"><use href="#icon-done"/></svg></li>
    <li class="entry"><p class="entry-title">Voluntary Check-in Request</p><p class="entry-meta">20 Oct 2018 10:27:59</p><svg class="entry-icon"><use href="#icon-done"/></svg></li>
    <li class="entry"><p class="entry-title">Voluntary Check-in Request</p><p class="entry-meta">20 Oct 2018 10:27:59</p><svg class="entry-icon"><use href="#icon-pin"/></svg></li>
  </ul>
  <nav class="tab-bar">
    <div class="tab"><svg><use href="#icon-home"/></svg>Home</div>
    <div class="tab tab--active"><svg><use href="#icon-checkin"/></svg>Check-ins</div>
    <div class="tab"><svg><use href="#icon-map"/></svg>Map</div>
    <div class="tab"><svg><use href="#icon-info"/></svg>Info</div>
  </nav>
</section>

<section class="screen screen--court">
  <header class="top-bar">
    <svg class="menu-icon"><use href="#icon-menu"/></svg>
    <span class="user-name">Marcus D Ellery</span>
    <div class="avatar" role="img" aria-label="User profile photo"></div>
  </header>
  <h1 class="page-title">Court Dates</h1>
  <ul class="entry-list">
    <li class="entry"><p class="entry-title entry-title--date">Friday, Oct 12th at 9:00 a.m.</p><p class="entry-meta">Harlow County Circuit Court Room 105</p><svg class="entry-icon"><use href="#icon-video"/></svg></li>
    <li class="entry"><p class="entry-title entry-title--date">Thursday, Sep 3rd at 1:00 p.m.</p><p class="entry-meta">Fernbrook District Court</p><svg class="entry-icon"><use href="#icon-done"/></svg></li>
    <li class="entry"><p class="entry-title entry-title--date">Thursday, Aug 8th at 2:00 p.m.</p><p class="entry-meta">Fernbrook District Court</p><svg class="entry-icon"><use href="#icon-video"/></svg></li>
    <li class="entry"><p class="entry-title entry-title--date">Thursday, Jul 4th at 1:00 p.m.</p><p class="entry-meta">Fernbrook District Court</p><svg class="entry-icon"><use href="#icon-done"/></svg></li>
    <li class="entry"><p class="entry-title entry-title--date">Thursday, Jun 6th at 3:00 p.m.</p><p class="entry-meta">Fernbrook District Court</p><svg class="entry-icon"><use href="#icon-done"/></svg></li>
    <li class="entry"><p class="entry-title entry-title--date">Thursday, Apr 2nd at 2:00 p.m.</p><p class="entry-meta">Fernbrook District Court</p><svg class="entry-icon"><use href="#icon-done"/></svg></li>
    <li class="entry"><p class="entry-title entry-title--date">Thursday, Mar 3rd at 1:00 p.m.</p><p class="entry-meta">Fernbrook District Court</p><svg class="entry-icon"><use href="#icon-done"/></svg></li>
    <li class="entry"><p class="entry-title entry-title--date">Thursday, Feb 5th at 1:00 p.m.</p><p class="entry-meta">Fernbrook District Court</p><svg class="entry-icon"><use href="#icon-video"/></svg></li>
  </ul>
  <nav class="tab-bar">
    <div class="tab"><svg><use href="#icon-home"/></svg>Home</div>
    <div class="tab tab--active"><svg><use href="#icon-checkin"/></svg>Check-ins</div>
    <div class="tab"><svg><use href="#icon-map"/></svg>Map</div>
    <div class="tab"><svg><use href="#icon-info"/></svg>Info</div>
  </nav>
</section>

</body>
</html>
```